EILT: Landing Page - EXPRESS VERSAND
Zielgruppe
Es soll in kurzer Zeit (max 48 Stunden) eine kleine Ladingpage entstehen. Expressversand / Import von China nach Deutschland . Aufgrund der stark steigenden Luftfrachtraten aus China heraus hat sich unsere Firma Fracht-Kapazitäten gesichert. Diese sollen nun angeboten werden. Über eine Ladingpage sollen Anfragen generiert werden. Diese Anfragen werden dann mit einem Angebot von uns beantwortet. Expressversand / Import von China nach Deutschland
Aufgabenstellung
Die Seite soll beinhalten:
- 1-2 Bilder (z. B. Luftfracht, Logistik, Flugzeug, Cargo, etc)
- kurzer erklärender Text: z.B. 'jetzt Angebot anfordern und günstig aus China per Express versenden.' Inkl. Abholung, Verzollung und Zustellung. Kurze Laufzeit von nur 3-5 Tagen. ab 45€ / Paket
- Anfrage Formular, bestehend aus: , Abholadresse in China/Post Code, ZielAdresse Deutschland, Sendungsinformationen (wie viele Kartons, wie schwer ist ein Karton und welche Abmessungen L/B/H ), wann ist die Sendung in China abholbereit, optional: Sendungsinhalt (Ware, Zolltarifnummer/HS Code) , Firma, Name, email adresse
- optional ein Header/Laufband etc mit: Bis zum 19. Nov 21 versenden - Ware bis MegaSonntag erhalten!
- 24h Servicehotline, Tel: 0987/314265
- 2-3 Kundenreferenzen: Bilder von Personen mit Text : „Schneller Versand - nur 4 Tage Laufzeit“ , „1A Service, ohne Probleme“ , „gute Preise - nur zu empfehlen.“
Unser Firmenlogo kann - muss aber nicht auftauchen.
In der farblichen Gestaltung haben Sie freie Hand und freuen uns auf Ihre Vorschläge.
Aufgrund der Dringlichkeit sollte diese Landingpage innerhalb 48 Stunden 'live ' gehen.
WICHTIG: Die Page sollte von Ihnen auch veröffentlich werden. Aktuell nutzen wir den Kelvo Homepagebaukasten. Die Page kann aber auch durch andere Anbieter veröffentlicht werden , zb Pagerune

```html
<!DOCTYPE html>
<html lang="de">
<head>
<meta charset="utf-8">
<title>Expressversand China – Deutschland</title>
<link rel="stylesheet" href="https://fonts.googleapis.com/css2?family=Source+Sans+3:wght@400;600;700&display=swap">
<style>
:root{
  --violet:#6a12f0;
  --violet-text:#6a1ad8;
  --indigo:#3d22b5;
  --ink-blue:#3a25a8;
  --rust:#c84a3a;
  --white:#ffffff;
  --field-border:#7a7a7a;
  --star:#f4b31c;
  --quote:#5a1a9a;
}
*{margin:0;padding:0;box-sizing:border-box}
html,body{width:1158px;height:1200px;overflow:hidden}
body{font-family:"Source Sans 3",sans-serif;background:var(--white);position:relative;color:#222}
.promo-bar{position:absolute;left:0;top:0;width:1158px;height:51px;background:var(--white);display:flex;align-items:center;justify-content:center;color:var(--violet-text);font-size:18px;font-weight:600;box-shadow:0 2px 4px rgba(0,0,0,.15);z-index:2}
.hero{position:absolute;left:0;top:51px;width:1158px;height:1105px;background:linear-gradient(120deg,var(--violet) 0%,#8a24c4 45%,var(--rust) 100%)}
.brand{position:absolute;left:148px;top:76px;display:flex;align-items:center;gap:8px;color:var(--white);font-size:28px;font-weight:700}
.brand-dot{width:34px;height:34px;border-radius:50%;background:#e86a8a}
.headline{position:absolute;left:145px;top:198px;color:var(--white);font-size:41px;font-weight:700;line-height:42px}
.hotline-label{position:absolute;left:148px;width:266px;top:386px;text-align:center;color:var(--white);font-size:18px;font-weight:600}
.hotline{position:absolute;left:148px;top:416px;width:266px;height:44px;border-radius:22px;background:var(--rust);color:var(--white);display:flex;align-items:center;padding-left:24px;gap:8px;font-size:27px;font-weight:700}
.visual-circle{position:absolute;left:598px;top:62px;width:412px;height:412px;border-radius:50%;background:var(--indigo)}
.visual-scene{position:absolute;left:496px;top:130px;width:590px;height:300px;border-radius:10px;background:linear-gradient(90deg,#1f4f6a 0%,#c9904f 55%,#e8e8ee 100%);opacity:.9}
.pointer{position:absolute;left:186px;top:486px}
.request-card{position:absolute;left:145px;top:508px;width:868px;height:375px;background:var(--white);border-radius:3px}
.request-intro{position:absolute;left:93px;top:18px;width:760px;color:var(--ink-blue);font-size:21px;font-weight:600;line-height:29px}
.request-intro .accent{color:var(--rust)}
.field{position:absolute;width:240px;height:38px;border:2px solid var(--field-border);border-radius:4px;display:flex;align-items:center;padding-left:14px;font-size:13px;color:#222}
.send-button{position:absolute;left:315px;top:299px;width:245px;height:39px;border-radius:20px;background:var(--rust);color:var(--white);display:flex;align-items:center;justify-content:center;gap:10px;font-size:17px;font-weight:600}
.quote-mark{position:absolute;left:144px;top:900px;color:var(--quote);font-size:120px;font-weight:700;line-height:1}
.reviews-title{position:absolute;left:0;width:1158px;top:934px;text-align:center;color:var(--white);font-size:27px;font-weight:600}
.review{position:absolute;top:1002px;width:279px;height:122px;background:rgba(60,10,90,.22);color:var(--white);text-align:center}
.review-text{margin-top:16px;font-size:14.5px}
.review-author{display:flex;align-items:center;justify-content:center;gap:8px;margin-top:14px}
.avatar{width:52px;height:52px;border-radius:50%;background:linear-gradient(135deg,#5a4a48,#c9a58e)}
.author-meta{text-align:left;font-size:12px;line-height:17px}
.stars{color:var(--star);font-size:11px;letter-spacing:1px}
.footer{position:absolute;left:0;top:1156px;width:1158px;height:44px;display:flex;align-items:center;justify-content:center;font-size:12.5px;color:#222}
</style>
</head>
<body>
<div class="promo-bar">noch bis 19. November versenden und Sendung bis MegaSonntag herhalten!</div>

<section class="hero">
</section>

<div class="brand"><span class="brand-dot"></span>Ferlo</div>

<h1 class="headline">Expressversand /<br>Import von China<br>nach Deutschland</h1>

<div class="hotline-label">24h Servicehotline</div>
<div class="hotline">
  <svg width="24" height="24" viewBox="0 0 24 24" fill="none" stroke="#fff" stroke-width="1.8"><path d="M5 3h4l2 5-3 2a12 12 0 0 0 6 6l2-3 5 2v4a2 2 0 0 1-2 2A18 18 0 0 1 3 5a2 2 0 0 1 2-2z"/><path d="M15 3a6 6 0 0 1 6 6M15 7a2 2 0 0 1 2 2"/></svg>
  0987/314265
</div>

<div class="visual-circle"></div>
<div class="visual-scene" role="img" aria-label="Frachtflugzeug, Containerschiff, Gabelstapler mit Kartons, Lieferwagen und LKW"></div>

<svg class="pointer" width="46" height="102" viewBox="0 0 46 102" fill="none" stroke="#c84a3a" stroke-width="4" stroke-linecap="round"><path d="M34 12C26 -2 18 4 18 30c0 25 2 45 6 66"/><path d="M6 72l18 26 12-28"/></svg>

<section class="request-card">
  <p class="request-intro">Jetzt Angebot anfordern und günstig aus China per Express versenden.' Inkl. Abholung, Verzollung und Zustellung. Kurze Laufzeit von nur <span class="accent">3-5 Tagen.</span><br>ab <span class="accent">45€ / Paket</span></p>

  <div class="field" style="left:50px;top:123px">Firma</div>
  <div class="field" style="left:316px;top:123px">Name</div>
  <div class="field" style="left:578px;top:123px">Email Adresse</div>
  <div class="field" style="left:50px;top:178px">Abholadresse in China</div>
  <div class="field" style="left:316px;top:178px">Post Code</div>
  <div class="field" style="left:578px;top:178px">ZielAdresse Deutschland</div>
  <div class="field" style="left:50px;top:231px">Wie Viele Kartons</div>
  <div class="field" style="left:316px;top:231px">Karton Gewicht</div>
  <div class="field" style="left:578px;top:231px">Abmessungen&nbsp; L / W / H</div>

  <div class="send-button">
    <svg width="18" height="18" viewBox="0 0 24 24" fill="none" stroke="#fff" stroke-width="1.6"><path d="M22 2L2 12l8 3 3 7 9-20zM10 15l12-13"/></svg>
    SENDEN
  </div>
</section>

<div class="quote-mark">“</div>
<h2 class="reviews-title">Was under Kunde sagt</h2>

<div class="review" style="left:148px">
  <p class="review-text">Schneller Versand - nur 4 Tage Laufzeit</p>
  <div class="review-author"><div class="avatar" role="img" aria-label="Kundenfoto"></div><div class="author-meta">Tarek Olm<div class="stars">★★★★★</div></div></div>
</div>
<div class="review" style="left:440px">
  <p class="review-text">1A Service, ohne Probleme</p>
  <div class="review-author"><div class="avatar" role="img" aria-label="Kundenfoto"></div><div class="author-meta">Jonas Deller<div class="stars">★★★★★</div></div></div>
</div>
<div class="review" style="left:733px">
  <p class="review-text">Gute Preise - nur zu empfehlen.</p>
  <div class="review-author"><div class="avatar" role="img" aria-label="Kundenfoto"></div><div class="author-meta">Tarek Olm<div class="stars">★★★★★</div></div></div>
</div>

<footer class="footer">Copyright 2021. Alle Rechte vorbehalten.</footer>
</body>
</html>
```